Briney Lark Fare landing page design

We need a landing page designed for an ecommerce website that sales fresh US domestic shrimp from the Gulf of Mexico and ships them direct to the consumer "From Our Shore To Your Door". For the landing page, we would like customers to be able to place an order and or inquire further about our product as well as links to social media. The company logo is attached

1 page

```html
<!DOCTYPE html>
<html lang="en">
<head>
<meta charset="utf-8">
<title>Briney Lark Fare – Wild-Caught Gulf Shrimp</title>
<link rel="stylesheet" href="https://fonts.googleapis.com/css2?family=Open+Sans:wght@400;600;700&family=Oswald:wght@400;500&family=Signika:wght@500;600&display=swap">
<style>
:root{
  --orange:#ee8748;
  --orange-dark:#e2733a;
  --ink:#3a3a3a;
  --muted:#8a8a8a;
  --steel:#8eaecb;
  --steel-dark:#6f93b5;
  --line:#e4e4e4;
  --white:#ffffff;
}
*{box-sizing:border-box;margin:0;padding:0}
html,body{width:768px;height:1200px;overflow:hidden;background:var(--white)}
body{font-family:"Open Sans",sans-serif;color:var(--ink);position:relative}
.page{position:relative;width:768px;height:1200px;overflow:hidden}
.abs{position:absolute}

/* brand */
.brand{display:flex;align-items:center;gap:5px}
.brand-dot{width:30px;height:30px;border-radius:50%;border:2px solid var(--steel);flex:none}
.brand-name{font-family:"Signika",sans-serif;font-weight:600;font-size:11px;color:#4b5560;letter-spacing:1.5px;line-height:11px;text-transform:uppercase;width:62px}

/* header */
.site-header{left:0;top:0;width:768px;height:48px;background:var(--white)}
.site-header .brand{position:absolute;left:103px;top:8px}
.header-contact{position:absolute;right:108px;top:18px;display:flex;align-items:center;gap:10px;font-size:8px;color:#555}
.header-contact .item{display:flex;align-items:center;gap:4px}
.sep{width:1px;height:10px;background:var(--line)}
.social-mini{display:flex;gap:8px}
.social-mini span{width:8px;height:8px;border-radius:50%;background:#9aa5b0}
.social-mini span:first-child{background:var(--orange)}

/* hero */
.hero{left:0;top:48px;width:768px;height:325px}
.hero-photo{position:absolute;inset:0;background:linear-gradient(160deg,#4b5764 0%,#3a4754 35%,#57626a 65%,#3b4650 100%)}
.hero-wave{position:absolute;left:0;bottom:0}
.hero-copy{position:absolute;left:103px;top:115px;color:var(--white)}
.hero-copy h1{font-family:"Signika",sans-serif;font-weight:500;font-size:19px;line-height:22px}
.hero-copy p{font-size:7px;line-height:12px;margin-top:8px;width:270px}
.btn-outline-light{display:inline-block;margin-top:10px;border:1.5px solid var(--white);border-radius:10px;padding:3px 14px;font-size:6.5px;font-weight:700;color:var(--white)}
.shrimp-art{left:104px;top:298px;width:250px;height:112px;border-radius:60px 40px 60px 20px;background:radial-gradient(ellipse at 40% 40%,#f79b4f,#e8622a 70%)}

/* enquiry */
.enquiry{left:487px;top:105px;width:178px;height:222px;background:var(--white);box-shadow:0 2px 8px rgba(0,0,0,.2)}
.enquiry-head{background:var(--orange);height:61px;padding:7px 14px;color:var(--white)}
.enquiry-head h2{font-family:"Signika",sans-serif;font-weight:500;font-size:11px;display:flex;align-items:center;gap:4px}
.enquiry-head p{font-size:5.6px;line-height:10px;margin-top:5px}
.enquiry-form{padding:13px 14px 0}
.field{height:16px;border:1px solid var(--line);background:#fafafa;font-size:6px;color:#999;padding:3px 7px;margin-bottom:5.5px}
.field.message{height:47px}
.btn-submit{height:17px;background:var(--orange);color:var(--white);font-size:6.5px;font-weight:700;text-align:center;line-height:17px;margin-top:9px}

/* products */
.products-title{left:0;top:418px;width:768px;text-align:center;font-family:"Oswald",sans-serif;font-weight:400;font-size:15px;color:#444}
.products-intro{left:150px;top:442px;width:468px;text-align:center;font-size:6.8px;line-height:12px;color:var(--muted)}
.product-grid{left:24px;top:487px;display:flex;gap:9.6px}
.product-card{width:112px;height:173px;background:var(--white);box-shadow:0 1px 5px rgba(0,0,0,.15);position:relative;text-align:center}
.product-photo{height:73px}
.product-label{position:absolute;left:12px;top:64px;width:88px;height:15px;background:var(--steel);color:var(--white);font-family:"Signika",sans-serif;font-size:7.5px;line-height:15px;clip-path:polygon(7px 0,calc(100% - 7px) 0,100% 50%,calc(100% - 7px) 100%,7px 100%,0 50%)}
.product-card p{font-size:6.4px;line-height:12px;color:var(--muted);padding:12px 8px 0}
.btn-order{display:inline-block;margin-top:10px;border:1px solid var(--orange);color:var(--orange);border-radius:8px;font-size:6px;font-weight:700;padding:2px 10px}
.btn-order.solid{background:var(--orange);color:var(--white)}

/* banner */
.delivery-banner{left:103px;top:698px;width:562px;height:115px;background:linear-gradient(90deg,#2c3136 0%,#3e464e 50%,#545b62 100%)}
.delivery-banner h2{position:absolute;left:24px;top:40px;font-family:"Oswald",sans-serif;font-weight:500;font-size:13px;line-height:18px;color:var(--white)}
.btn-steel{position:absolute;left:375px;top:48px;width:165px;height:18px;border-radius:9px;background:var(--steel);color:var(--white);font-size:7px;font-weight:700;text-align:center;line-height:18px}

/* about */
.about{left:0;top:851px;width:768px;height:194px;background:var(--orange)}
.about h2{position:absolute;left:103px;top:33px;font-family:"Oswald",sans-serif;font-weight:500;font-size:16px;color:var(--white)}
.about-text{position:absolute;left:103px;top:68px;width:315px;font-size:6.8px;line-height:13.6px;color:var(--white)}
.about-text p+p{margin-top:13px}
.about-photo{left:439px;top:851px;width:226px;height:155px;background:linear-gradient(135deg,#b9a98a 0%,#d9a25b 35%,#7b8ea6 70%,#aab3bd 100%);box-shadow:0 4px 10px rgba(0,0,0,.3)}

/* footer */
.site-footer .brand{position:absolute;left:103px;top:1083px}
.site-footer .brand-dot{width:36px;height:36px}
.site-footer .brand-name{font-size:12px;line-height:12px;width:70px}
.foot-col{top:1081px}
.foot-col h3{font-family:"Signika",sans-serif;font-weight:500;font-size:10px;color:#444;margin-bottom:9px}
.foot-col .line{font-size:7px;color:#555;display:flex;align-items:center;gap:5px;margin-bottom:4px}
.social-round{display:flex;gap:9px}
.social-round span{width:19px;height:19px;border-radius:50%;background:var(--steel)}
.social-round span:first-child{background:var(--orange)}
.foot-col p.small{font-size:6px;color:var(--muted)}
.subscribe{display:flex;margin-top:8px}
.subscribe .input{width:92px;height:16px;border:1px solid var(--line);font-size:6.5px;color:#777;display:flex;align-items:center;gap:4px;padding-left:5px}
.subscribe .send{width:38px;height:16px;background:var(--steel-dark);color:var(--white);font-size:7px;font-weight:700;text-align:center;line-height:16px}
.foot-rule{left:0;top:1169px;width:768px;height:1px;background:var(--line)}
.copyright{left:103px;top:1180px;font-size:6.3px;color:var(--muted)}
</style>
</head>
<body>
<div class="page">

  <header class="site-header abs">
    <div class="brand"><span class="brand-dot"></span><span class="brand-name">Briney Lark Fare</span></div>
    <div class="header-contact">
      <span class="item">
        <svg width="8" height="8" viewBox="0 0 10 10"><path d="M2 1l2 2-1 1.2c.6 1.2 1.6 2.2 2.8 2.8L7 6l2 2-1.3 1.3C4.5 9 1 5.5.7 2.3z" fill="none" stroke="#ee8748" stroke-width=".9"/></svg>
        +1 555 0142 778
      </span>
      <span class="sep"></span>
      <span class="item">
        <svg width="9" height="7" viewBox="0 0 9 7"><rect x=".5" y=".5" width="8" height="6" fill="none" stroke="#ee8748" stroke-width=".9"/><path d="M.5.5l4 3.2 4-3.2" fill="none" stroke="#ee8748" stroke-width=".9"/></svg>
        hello@brineylarkfare.com
      </span>
      <span class="sep"></span>
      <span class="social-mini"><span></span><span></span><span></span><span></span></span>
    </div>
  </header>

  <section class="hero abs">
    <div class="hero-photo" role="img" aria-label="Shrimp swimming in dark coastal water"></div>
    <svg class="hero-wave" width="768" height="40" viewBox="0 0 768 40" preserveAspectRatio="none"><path d="M0 20 C120 0 220 2 330 14 C460 28 560 8 768 20 L768 40 L0 40Z" fill="#fff"/></svg>
    <div class="hero-copy">
      <h1>The highest quality<br>wild-caught domestic shrimp</h1>
      <p>We sale fresh US domestic shrimp from the Gulf of Mexico and ships them direct to the consumer "From Our Shore To Your Door".</p>
      <span class="btn-outline-light">ORDER NOW</span>
    </div>
  </section>
  <div class="shrimp-art abs" role="img" aria-label="Cooked orange shrimp"></div>

  <aside class="enquiry abs">
    <div class="enquiry-head">
      <h2><svg width="9" height="9" viewBox="0 0 10 10"><circle cx="5" cy="5" r="4" fill="none" stroke="#fff" stroke-width="1"/><path d="M4 4a1 1 0 1 1 1.3 1L5 6" fill="none" stroke="#fff" stroke-width=".9"/></svg>Quick Enquiry</h2>
      <p>Got a question? Contact us quickly and easily using the following form and we'll get back to you ASAP</p>
    </div>
    <div class="enquiry-form">
      <div class="field">Your Name</div>
      <div class="field">Phone</div>
      <div class="field">Email</div>
      <div class="field message">Message</div>
      <div class="btn-submit">SUBMIT</div>
    </div>
  </aside>

  <h2 class="products-title abs">OUR PRODUCTS</h2>
  <p class="products-intro abs">Sed ut perspiciatis unde omnis iste natus error sit voluptatem accusantium doloremque laudantium, totam rem aperiam, eaque ipsa quae ab illo inventore veritatis et quasi architecto beatae vitae dicta sunt explicabo.</p>

  <div class="product-grid abs">
    <article class="product-card">
      <div class="product-photo" role="img" aria-label="Brown shrimp on white" style="background:linear-gradient(135deg,#eeeeee,#a38466 60%,#e9e6e2)"></div>
      <div class="product-label">Brown Shrimp</div>
      <p>Lorem ipsum dolor sit amet, consectetur adipiscing elit, sed do eiusmod tempor incididunt ut labore et dolore</p>
      <span class="btn-order solid">ORDER NOW</span>
    </article>
    <article class="product-card">
      <div class="product-photo" role="img" aria-label="Raw pink shrimp" style="background:linear-gradient(135deg,#c9566e,#e08a9b 50%,#b9475e)"></div>
      <div class="product-label">Pink Shrimp</div>
      <p>Lorem ipsum dolor sit amet, consectetur adipiscing elit, sed do eiusmod tempor incididunt ut labore et dolore</p>
      <span class="btn-order">ORDER NOW</span>
    </article>
    <article class="product-card">
      <div class="product-photo" role="img" aria-label="Maine shrimp" style="background:linear-gradient(135deg,#e36a32,#f2a06a 50%,#c9502a)"></div>
      <div class="product-label">Maine Shrimp</div>
      <p>Lorem ipsum dolor sit amet, consectetur adipiscing elit, sed do eiusmod tempor incididunt ut labore et dolore</p>
      <span class="btn-order">ORDER NOW</span>
    </article>
    <article class="product-card">
      <div class="product-photo" role="img" aria-label="Royal red shrimp" style="background:linear-gradient(135deg,#d3341c,#ee5a2f 50%,#b6261a)"></div>
      <div class="product-label">Royal Red Shrimp</div>
      <p>Lorem ipsum dolor sit amet, consectetur adipiscing elit, sed do eiusmod tempor incididunt ut labore et dolore</p>
      <span class="btn-order">ORDER NOW</span>
    </article>
    <article class="product-card">
      <div class="product-photo" role="img" aria-label="Spot prawns with lemon" style="background:linear-gradient(135deg,#efb190,#f4c8ac 50%,#e9d37a)"></div>
      <div class="product-label">Spot Prawns</div>
      <p>Lorem ipsum dolor sit amet, consectetur adipiscing elit, sed do eiusmod tempor incididunt ut labore et dolore</p>
      <span class="btn-order">ORDER NOW</span>
    </article>
    <article class="product-card">
      <div class="product-photo" role="img" aria-label="Hands holding white shrimp" style="background:linear-gradient(135deg,#6f8a80,#9aa99a 50%,#5e7470)"></div>
      <div class="product-label">White Shrimp</div>
      <p>Lorem ipsum dolor sit amet, consectetur adipiscing elit, sed do eiusmod tempor incididunt ut labore et dolore</p>
      <span class="btn-order">ORDER NOW</span>
    </article>
  </div>

  <section class="delivery-banner abs" role="img" aria-label="Fresh shrimp being sorted at the dock">
    <h2>WILD-CAUGHT FRESH US DOMESTIC SHRIMP<br>DELIVERED DIRECTLY TO YOU</h2>
    <span class="btn-steel">GET YOUR HOME DELIVERY</span>
  </section>

  <section class="about abs">
    <h2>ABOUT US</h2>
    <div class="about-text">
      <p>Nemo enim ipsam voluptatem quia voluptas sit aspernatur aut odit aut fugit, sed quia consequuntur magni dolores eos qui ratione voluptatem sequi nesciunt. Neque porro quisquam est, qui dolorem ipsum quia dolor sit amet, consectetur, adipisci velit, sed quia non numquam eius modi tempora incidunt ut labore et dolore magnam aliquam quaerat voluptatem.</p>
      <p>Ut enim ad minima veniam, quis nostrum exercitationem ullam corporis suscipit laboriosam, nisi ut aliquid ex ea commodi consequatur.</p>
    </div>
  </section>
  <div class="about-photo abs" role="img" aria-label="Worker in gloves sorting fresh shrimp into a basket"></div>

  <footer class="site-footer">
    <div class="brand"><span class="brand-dot"></span><span class="brand-name">Briney Lark Fare</span></div>
    <div class="foot-col abs" style="left:247px">
      <h3>Contact</h3>
      <div class="line"><svg width="8" height="8" viewBox="0 0 10 10"><path d="M2 1l2 2-1 1.2c.6 1.2 1.6 2.2 2.8 2.8L7 6l2 2-1.3 1.3C4.5 9 1 5.5.7 2.3z" fill="none" stroke="#ee8748" stroke-width=".9"/></svg>+1 555 0142 778</div>
      <div class="line"><svg width="9" height="7" viewBox="0 0 9 7"><rect x=".5" y=".5" width="8" height="6" fill="none" stroke="#ee8748" stroke-width=".9"/><path d="M.5.5l4 3.2 4-3.2" fill="none" stroke="#ee8748" stroke-width=".9"/></svg>hello@brineylarkfare.com</div>
    </div>
    <div class="foot-col abs" style="left:390px">
      <h3>Connect</h3>
      <div class="social-round"><span></span><span></span><span></span><span></span></div>
    </div>
    <div class="foot-col abs" style="left:535px">
      <h3>Subscribe</h3>
      <p class="small">Want our news sent directly to your inbox?</p>
      <div class="subscribe">
        <div class="input"><svg width="8" height="6" viewBox="0 0 9 7"><rect x=".5" y=".5" width="8" height="6" fill="none" stroke="#ee8748" stroke-width=".9"/><path d="M.5.5l4 3.2 4-3.2" fill="none" stroke="#ee8748" stroke-width=".9"/></svg>Your email address</div>
        <div class="send">SEND</div>
      </div>
    </div>
    <div class="foot-rule abs"></div>
    <p class="copyright abs">© 2019 Briney Lark Fare. All rights reserved.</p>
  </footer>

</div>
</body>
</html>
```